Digital Album Cover - Frosted Lanterns (Night Falls Still)

HiI need a digital album cover for a piano instrumental cover single

Artist: Corey Dalton
Title: Frosted Lanterns (Night Falls Still)

The song was originally by Derek Holloway

Please use my logo

You can listen to the track herehttps://soundcloud.com/coreydaltonkeys/frosted-lanterns-night-falls-still-piano-instrumental-cover

Requirements
Must have
• My logo design Corey Dalton

```html
<!DOCTYPE html>
<html lang="en">
<head>
<meta charset="utf-8">
<title>Frosted Lanterns (Night Falls Still) – Corey Dalton</title>
<link rel="stylesheet" href="https://fonts.googleapis.com/css2?family=Great+Vibes&family=Work+Sans:wght@400;600&display=swap">
<style>
  :root {
    --amber-glow: #f2b632;
    --deep-brown: #2a1608;
    --warm-brown: #6b3e12;
    --ember: #a8661c;
    --title-yellow: #f7ea6b;
    --ink-white: #ffffff;
  }
  html, body {
    margin: 0;
    padding: 0;
    width: 1200px;
    height: 1200px;
    overflow: hidden;
    background: var(--deep-brown);
  }
  .cover {
    position: relative;
    width: 1200px;
    height: 1200px;
    overflow: hidden;
    font-family: "Work Sans", Arial, sans-serif;
    color: var(--ink-white);
  }
  .cover__photo {
    position: absolute;
    inset: 0;
    background:
      radial-gradient(circle at 56% 72%, rgba(242,182,50,0.85) 0, rgba(242,182,50,0.35) 9%, transparent 22%),
      radial-gradient(ellipse at 22% 16%, rgba(242,182,50,0.55) 0, transparent 30%),
      radial-gradient(ellipse at 88% 44%, rgba(242,182,50,0.5) 0, transparent 28%),
      radial-gradient(ellipse at 50% 55%, rgba(30,14,4,0.85) 0, rgba(30,14,4,0.5) 30%, transparent 55%),
      linear-gradient(180deg, var(--ember) 0%, var(--warm-brown) 45%, var(--deep-brown) 100%);
  }
  .title {
    position: absolute;
    left: 0;
    width: 1200px;
    top: 240px;
    margin: 0;
    text-align: center;
    font-family: "Great Vibes", cursive;
    font-weight: 400;
    color: var(--title-yellow);
    line-height: 0.95;
  }
  .title__line {
    display: block;
    font-size: 118px;
  }
  .title__line--second {
    font-size: 112px;
  }
  .subtitle {
    position: absolute;
    left: 470px;
    top: 528px;
    margin: 0;
    font-size: 32px;
    font-weight: 400;
    letter-spacing: 0.5px;
    text-transform: uppercase;
  }
  .credit {
    position: absolute;
    left: 0;
    width: 1200px;
    top: 986px;
    margin: 0;
    text-align: center;
    font-size: 23px;
    font-weight: 600;
    letter-spacing: 0.6px;
    text-transform: uppercase;
  }
  .brand {
    position: absolute;
    left: 368px;
    top: 1057px;
    display: flex;
    align-items: center;
    gap: 22px;
  }
  .brand__mark {
    width: 102px;
    height: 102px;
    border-radius: 50%;
    background: var(--ink-white);
  }
  .brand__text {
    display: flex;
    flex-direction: column;
    align-items: center;
  }
  .brand__name {
    font-size: 36px;
    font-weight: 600;
    line-height: 1.1;
    text-transform: uppercase;
  }
  .brand__role {
    margin-top: 4px;
    font-size: 18px;
    font-weight: 400;
  }
</style>
</head>
<body>
  <main class="cover">
    <div class="cover__photo" role="img" aria-label="Warm amber photo of cupped hands holding a glowing mesh star fairy light, with blurred golden string lights and a faint silhouette of a figure saluting"></div>

    <h1 class="title">
      <span class="title__line">Frosted</span>
      <span class="title__line title__line--second">Lanterns</span>
    </h1>
    <p class="subtitle">Night Falls Still</p>

    <p class="credit">The song was originally by Derek Holloway</p>

    <div class="brand">
      <div class="brand__mark"></div>
      <div class="brand__text">
        <span class="brand__name">Corey Dalton</span>
        <span class="brand__role">Wedding &amp; Event Pianist</span>
      </div>
    </div>
  </main>
</body>
</html>
```